Tarvimoor business cards

Need fresh design for our business cards. Logo must be specific, we are open for everything else.

Contact Information for Business Card

phrase "GMP & JANITORIAL SERVICES" should be used as main point of card

Colors
3176b5
3276b5
85acd3
cedeed
ffffff
0292cd
33a6d7
85cae6
cee9f5

Requirements
Must have
• The logo
Should not have
• crowded designs

```html
<!DOCTYPE html>
<html lang="en">
<head>
<meta charset="utf-8">
<title>Tarvimoor Business Cards</title>
<link href="https://fonts.googleapis.com/css2?family=Marcellus&family=Open+Sans:wght@400;700&display=swap" rel="stylesheet">
<style>
  :root {
    --brand-blue: #1a93cf;
    --deep-blue: #3176b5;
    --sky-blue: #33a6d7;
    --ink: #1d1d1f;
    --white: #ffffff;
    --tint: #cee9f5;
    --backdrop: #e6e8e9;
  }
  * { margin: 0; padding: 0; box-sizing: border-box; }
  html, body { width: 1200px; height: 1200px; overflow: hidden; }
  body {
    background: var(--backdrop);
    font-family: "Marcellus", serif;
    position: relative;
  }
  .card {
    position: absolute;
    left: 170px;
    width: 860px;
    height: 525px;
    overflow: hidden;
    box-shadow: 0 10px 30px rgba(0,0,0,0.12);
  }
  .card--front { top: 50px; background: var(--white); }
  .card--back { top: 625px; background: var(--brand-blue); }

  .wordmark {
    position: absolute;
    font-family: "Marcellus", serif;
    font-size: 62px;
    letter-spacing: 6px;
    line-height: 1;
    display: flex;
    align-items: center;
    gap: 16px;
  }
  .wordmark__dot {
    width: 16px; height: 16px; border-radius: 50%;
    background: currentColor;
  }
  .card--front .wordmark { left: 60px; top: 150px; color: var(--deep-blue); }
  .card--back .wordmark { left: 0; right: 0; top: 222px; justify-content: center; color: var(--white); }

  .contact-list {
    position: absolute;
    left: 62px;
    top: 252px;
    list-style: none;
    font-size: 22px;
    color: var(--ink);
  }
  .contact-list li {
    display: flex;
    align-items: center;
    gap: 16px;
    height: 30px;
  }
  .contact-list .spacer { padding-left: 36px; }
  .icon { width: 20px; height: 20px; flex: none; }

  .wave { position: absolute; inset: 0; width: 100%; height: 100%; }

  .tagline {
    position: absolute;
    font-size: 21px;
    color: var(--tint);
    letter-spacing: 0.5px;
  }
  .card--front .tagline { left: 56px; top: 468px; }
  .card--back .tagline { left: 0; right: 0; top: 445px; text-align: center; }

  .person {
    position: absolute;
    left: 570px;
    width: 240px;
    top: 378px;
    text-align: center;
    color: var(--white);
    font-family: "Open Sans", sans-serif;
  }
  .person__name { font-weight: 700; font-size: 25px; line-height: 1.2; }
  .person__role { font-size: 23px; line-height: 1.2; color: var(--tint); }
  .person__phone {
    font-weight: 700; font-size: 24px; line-height: 1.25; letter-spacing: 1px;
    display: flex; align-items: center; justify-content: center; gap: 4px;
  }
  .person__phone .icon { width: 18px; height: 18px; }

  .back-links {
    position: absolute;
    left: 0; right: 0; top: 328px;
    display: flex; justify-content: center; gap: 10px;
    color: var(--white);
    font-size: 22px;
  }
  .back-links span { display: flex; align-items: center; gap: 8px; }
</style>
</head>
<body>

  <section class="card card--front" aria-label="Business card front">
    <svg class="wave" viewBox="0 0 650 396" preserveAspectRatio="none" aria-hidden="true">
      <path d="M0 300 C100 328 200 342 275 337" fill="none" stroke="var(--brand-blue)" stroke-width="5"/>
      <path d="M462 246 C520 218 590 210 650 222 L650 232 C590 222 525 230 470 252 Z" fill="var(--brand-blue)"/>
      <path d="M0 322 C120 346 250 366 360 326 C450 292 520 240 650 238 L650 396 L0 396 Z" fill="var(--brand-blue)"/>
    </svg>

    <div class="wordmark"><span>TARVIMOOR</span><span class="wordmark__dot"></span></div>

    <ul class="contact-list">
      <li>
        <svg class="icon" viewBox="0 0 20 20"><circle cx="10" cy="10" r="10" fill="var(--deep-blue)"/><path d="M6.5 5.5l2 0 1 2.5-1.3 1a6 6 0 0 0 3 3l1-1.3 2.5 1v2c-4.5 .5-8.7-3.7-8.2-8.2z" fill="#fff"/></svg>
        (555) 014-7731
      </li>
      <li>
        <svg class="icon" viewBox="0 0 20 20"><circle cx="10" cy="10" r="10" fill="var(--deep-blue)"/><rect x="5" y="6.5" width="10" height="7" fill="#fff"/><path d="M5 6.5l5 4 5-4" fill="none" stroke="var(--deep-blue)" stroke-width="1"/></svg>
        info@tarvimoor.com
      </li>
      <li>
        <svg class="icon" viewBox="0 0 20 20"><circle cx="10" cy="10" r="10" fill="var(--deep-blue)"/><path d="M10 4a4 4 0 0 0-4 4c0 3 4 8 4 8s4-5 4-8a4 4 0 0 0-4-4z" fill="#fff"/><circle cx="10" cy="8" r="1.5" fill="var(--deep-blue)"/></svg>
        50 Linden Road
      </li>
      <li class="spacer">Ashcombe wc 06180</li>
      <li>
        <svg class="icon" viewBox="0 0 20 20"><circle cx="10" cy="10" r="10" fill="var(--deep-blue)"/><circle cx="10" cy="10" r="4.5" fill="none" stroke="#fff" stroke-width="1.6"/><circle cx="10" cy="10" r="1.6" fill="#fff"/></svg>
        www.tarvimoor.com
      </li>
    </ul>

    <div class="person">
      <p class="person__name">ABC XXXXX</p>
      <p class="person__role">Managing Directow</p>
      <p class="person__phone">
        <svg class="icon" viewBox="0 0 20 20"><circle cx="10" cy="10" r="10" fill="#fff"/><rect x="7" y="4.5" width="6" height="11" rx="1" fill="var(--brand-blue)"/></svg>
        555 410 2286
      </p>
    </div>

    <p class="tagline">GMP &amp; JANITORIAL SERVICES</p>
  </section>

  <section class="card card--back" aria-label="Business card back">
    <div class="wordmark"><span>TARVIMOOR</span><span class="wordmark__dot"></span></div>

    <div class="back-links">
      <span>
        <svg class="icon" viewBox="0 0 20 20"><circle cx="10" cy="10" r="10" fill="#fff"/><rect x="5" y="6.5" width="10" height="7" fill="var(--brand-blue)"/></svg>
        info@tarvimoor.com
      </span>
      <span>
        <svg class="icon" viewBox="0 0 20 20"><circle cx="10" cy="10" r="10" fill="#fff"/><circle cx="10" cy="10" r="4.5" fill="none" stroke="var(--brand-blue)" stroke-width="1.6"/></svg>
        www.tarvimoor.com
      </span>
    </div>

    <p class="tagline">GMP &amp; JANITORIAL SERVICES</p>
  </section>

</body>
</html>
```